Business Card Design - Pediatric Dentist

We need a business card for a new dental office. We are a pediatric dentist in Austin Tx. I would like a design that use bright green and if possible light blue.

Target Market(s)

Marketed to young moms

Industry/Entity Type

Dental

Contact Information for Business Card

Marcus Hollin DDS
Tidewell Pediatric Dentistry
438 E. Corvell Lane. Austin TX 78731
(512) 284 9153.

In the back i would like to state "we take most insurances, Chip & Medicaid" & a map

Colors
add136
cadf82
85cae6

```html
<!DOCTYPE html>
<html lang="en">
<head>
<meta charset="utf-8">
<title>Tidewell Pediatric Dentistry – Business Card</title>
<link rel="stylesheet" href="https://fonts.googleapis.com/css2?family=Mouse+Memoirs&family=Nunito:wght@800&family=Noto+Serif:wght@400&display=swap">
<style>
  :root {
    --green-bright: #add136;
    --green-soft: #cadf82;
    --green-deep: #3aa635;
    --blue-light: #85cae6;
    --blue-fill: #9ccde2;
    --white: #ffffff;
  }
  html, body {
    margin: 0;
    padding: 0;
    width: 1200px;
    height: 686px;
    overflow: hidden;
    background: var(--white);
  }
  .card {
    position: relative;
    width: 1200px;
    height: 686px;
    background: var(--white);
    overflow: hidden;
  }
  .card__wave {
    position: absolute;
    inset: 0;
    width: 1200px;
    height: 686px;
  }
  .card__mascot {
    position: absolute;
    left: 37px;
    top: 133px;
    width: 283px;
    height: 290px;
    border-radius: 24px;
    background: radial-gradient(ellipse at 50% 45%, #f6f8f3 0%, #dcecd3 55%, #9fd08f 100%);
  }
  .card__doctor {
    position: absolute;
    right: 23px;
    top: 112px;
    margin: 0;
    font-family: "Nunito", sans-serif;
    font-weight: 800;
    font-size: 38px;
    line-height: 1;
    color: var(--blue-light);
  }
  .card__practice {
    position: absolute;
    right: 45px;
    top: 180px;
    margin: 0;
    font-family: "Mouse Memoirs", sans-serif;
    font-weight: 400;
    font-size: 97px;
    line-height: 1;
    color: var(--green-bright);
    letter-spacing: 1px;
    white-space: nowrap;
  }
  .card__address {
    position: absolute;
    left: 37px;
    top: 528px;
    margin: 0;
    font-family: "Noto Serif", serif;
    font-weight: 400;
    font-size: 41px;
    line-height: 62px;
    color: var(--white);
    font-style: normal;
    white-space: nowrap;
  }
</style>
</head>
<body>
  <main class="card">
    <svg class="card__wave" viewBox="0 0 1200 686" aria-hidden="true">
      <path d="M0 340 C 300 330, 700 420, 1200 560 L1200 686 L0 686 Z" fill="var(--blue-fill)"/>
      <path d="M0 298 C 300 290, 700 380, 1200 525" fill="none" stroke="var(--green-soft)" stroke-width="14"/>
    </svg>

    <div class="card__mascot" role="img" aria-label="Cartoon tooth mascot illustration"></div>

    <p class="card__doctor">Marcus Hollin DDS</p>
    <h1 class="card__practice">Tidewell Pediatric Dentistry</h1>

    <address class="card__address">
      438 E. Corvell Lane, Austin TX<br>
      78731 (512) 284 9153
    </address>
  </main>
</body>
</html>
```